Property investment company needs a letterhead design!

We are a new residential and commercial property investment company. Name of the company is Morvesta Group, LLC. We have a new logo and now we need letterhead! We prefer to have a professional and upscale appearance. We don't have any fixed requirements, so be creative! Thank you for considering this project. We are so excited to see what happens!

Target Market(s)

Professional

Industry/Entity Type

Real Estate Development

```html
<!DOCTYPE html>
<html lang="en">
<head>
<meta charset="utf-8">
<title>Morvesta Group, LLC — Letterhead</title>
<link href="https://fonts.googleapis.com/css2?family=Poppins:wght@300;400;500;600&family=Kaushan+Script&display=swap" rel="stylesheet">
<style>
  :root {
    --backdrop: #454545;
    --paper: #ffffff;
    --navy: #14233f;
    --blue: #00a0e3;
    --sky: #9fd8f2;
    --mist: #d3ecf9;
    --ink: #1c1c1c;
  }
  html, body { margin: 0; padding: 0; width: 1200px; height: 1200px; overflow: hidden; background: var(--backdrop); }
  .letterhead {
    position: absolute; left: 189px; top: 69px; width: 821px; height: 1061px;
    background: var(--paper); overflow: hidden;
    font-family: "Poppins", sans-serif; color: var(--ink);
  }
  .header-waves { position: absolute; left: 0; top: 0; }
  .brand-badge {
    position: absolute; left: 46px; top: 20px; width: 146px; height: 146px; border-radius: 50%;
    background: var(--paper); display: flex; align-items: center; justify-content: center;
  }
  .brand-name { font-family: "Poppins", sans-serif; font-weight: 600; color: var(--navy); font-size: 15px; text-align: center; line-height: 1.25; }
  .date-field { position: absolute; left: 573px; top: 139px; font-size: 15px; line-height: 20px; }
  .date-line { position: absolute; left: 621px; top: 152px; width: 106px; border-top: 1px solid var(--ink); }
  .line { position: absolute; left: 73px; font-size: 13.7px; line-height: 20px; white-space: nowrap; }
  .line.intro { font-weight: 500; left: 75px; }
  .line.heading { font-weight: 600; font-size: 13.7px; }
  .line.heading-lg { font-weight: 600; font-size: 17px; line-height: 22px; }
  .line.item { left: 105px; }
  .tick { position: absolute; left: 75px; width: 15px; height: 15px; }
  .regards { position: absolute; left: 73px; top: 819px; font-size: 17px; font-weight: 300; color: #333; }
  .signature { position: absolute; left: 66px; top: 848px; font-family: "Kaushan Script", cursive; font-size: 30px; color: #2a2a2a; }
  .footer-rule { position: absolute; left: 0; top: 969px; width: 705px; height: 6px; background: var(--navy); }
  .footer-badge {
    position: absolute; left: 706px; top: 926px; width: 86px; height: 86px; border-radius: 50%;
    background: var(--paper); display: flex; align-items: center; justify-content: center;
  }
  .footer-badge .brand-name { font-size: 11px; }
  .contact { position: absolute; top: 1000px; font-size: 12.4px; line-height: 15px; color: var(--navy); white-space: nowrap; }
  .contact-icon { position: absolute; }
  .divider { position: absolute; top: 998px; width: 1px; height: 26px; background: var(--navy); }
</style>
</head>
<body>
<main class="letterhead">
  <svg class="header-waves" width="821" height="170" viewBox="0 0 821 170" aria-hidden="true">
    <path d="M0 0 H821 V100 C600 55 380 70 0 122 Z" fill="var(--blue)"/>
    <path d="M276 77 C520 70 700 100 821 155 V120 C700 85 520 68 276 77 Z" fill="var(--mist)"/>
    <path d="M276 77 C520 66 700 85 821 135 V100 C700 70 520 62 276 77 Z" fill="var(--sky)"/>
    <path d="M0 0 H821 V73 C650 35 400 40 0 111 Z" fill="var(--navy)"/>
  </svg>
  <div class="brand-badge"><div class="brand-name">Morvesta<br>Group, LLC</div></div>

  <div class="date-field">Date:</div>
  <div class="date-line"></div>

  <div class="line intro" style="top:227px">Lorem Ipsum is simply dummy text of the printing and typesetting industry. Lorem Ipsum has been</div>

  <svg class="tick" style="top:268px" viewBox="0 0 16 16" aria-hidden="true"><rect x="1" y="3" width="12" height="12" rx="2" fill="none" stroke="var(--navy)" stroke-width="2"/><path d="M4 8 L7 11 L15 2" fill="none" stroke="var(--navy)" stroke-width="2.6"/></svg>
  <div class="line item" style="top:265px">Lorem Ipsum is simply</div>
  <svg class="tick" style="top:291px" viewBox="0 0 16 16" aria-hidden="true"><rect x="1" y="3" width="12" height="12" rx="2" fill="none" stroke="var(--navy)" stroke-width="2"/><path d="M4 8 L7 11 L15 2" fill="none" stroke="var(--navy)" stroke-width="2.6"/></svg>
  <div class="line item" style="top:288px">Lorem Ipsum is simply</div>
  <svg class="tick" style="top:315px" viewBox="0 0 16 16" aria-hidden="true"><rect x="1" y="3" width="12" height="12" rx="2" fill="none" stroke="var(--navy)" stroke-width="2"/><path d="M4 8 L7 11 L15 2" fill="none" stroke="var(--navy)" stroke-width="2.6"/></svg>
  <div class="line item" style="top:312px">Lorem Ipsum is simply</div>

  <div class="line heading" style="top:351px">Initial Access</div>
  <div class="line" style="top:378px">Lorem Ipsum is simply dummy text of the printing and typesetting industry. Lorem Ipsum has been the</div>
  <div class="line" style="top:402px">industry's standard dummy text ever since the 1500s, when an unknown printer took a galley of type and</div>
  <div class="line" style="top:426px">scrambled it to make a type specimen book. It has survived not only five centuries, but also the leap into</div>

  <div class="line heading" style="top:470px;left:71px">Execution</div>
  <div class="line" style="top:493px">Lorem Ipsum is simply dummy text of the printing and</div>
  <svg class="tick" style="top:525px" viewBox="0 0 16 16" aria-hidden="true"><rect x="1" y="3" width="12" height="12" rx="2" fill="none" stroke="var(--navy)" stroke-width="2"/><path d="M4 8 L7 11 L15 2" fill="none" stroke="var(--navy)" stroke-width="2.6"/></svg>
  <div class="line item" style="top:522px">Lorem Ipsum is simply</div>
  <svg class="tick" style="top:549px" viewBox="0 0 16 16" aria-hidden="true"><rect x="1" y="3" width="12" height="12" rx="2" fill="none" stroke="var(--navy)" stroke-width="2"/><path d="M4 8 L7 11 L15 2" fill="none" stroke="var(--navy)" stroke-width="2.6"/></svg>
  <div class="line item" style="top:546px">Lorem Ipsum is simply</div>
  <svg class="tick" style="top:573px" viewBox="0 0 16 16" aria-hidden="true"><rect x="1" y="3" width="12" height="12" rx="2" fill="none" stroke="var(--navy)" stroke-width="2"/><path d="M4 8 L7 11 L15 2" fill="none" stroke="var(--navy)" stroke-width="2.6"/></svg>
  <div class="line item" style="top:570px">Lorem Ipsum is simply</div>

  <div class="line heading-lg" style="top:615px;left:71px">Capabilties</div>
  <div class="line" style="top:643px">Lorem Ipsum is simply dummy text of the printing and</div>
  <svg class="tick" style="top:676px" viewBox="0 0 16 16" aria-hidden="true"><rect x="1" y="3" width="12" height="12" rx="2" fill="none" stroke="var(--navy)" stroke-width="2"/><path d="M4 8 L7 11 L15 2" fill="none" stroke="var(--navy)" stroke-width="2.6"/></svg>
  <div class="line item" style="top:673px">Lorem Ipsum is simply dummy text of the printing and typesetting industry. Lorem Ipsum</div>
  <svg class="tick" style="top:703px" viewBox="0 0 16 16" aria-hidden="true"><rect x="1" y="3" width="12" height="12" rx="2" fill="none" stroke="var(--navy)" stroke-width="2"/><path d="M4 8 L7 11 L15 2" fill="none" stroke="var(--navy)" stroke-width="2.6"/></svg>
  <div class="line item" style="top:700px">Lorem Ipsum is simply dummy text of the</div>
  <svg class="tick" style="top:731px" viewBox="0 0 16 16" aria-hidden="true"><rect x="1" y="3" width="12" height="12" rx="2" fill="none" stroke="var(--navy)" stroke-width="2"/><path d="M4 8 L7 11 L15 2" fill="none" stroke="var(--navy)" stroke-width="2.6"/></svg>
  <div class="line item" style="top:728px">Lorem Ipsum is simply dummy text of the printing and typesetting industry.</div>
  <div class="line item" style="top:753px">Lorem Ipsum has been the industry's standard dummy text ever since the</div>
  <div class="line item" style="top:776px">1500s, when an unknown printer took a galley of type and scrambled it to</div>

  <div class="regards">Warm Regards</div>
  <div class="signature">Dale Corwin</div>

  <div class="footer-rule"></div>
  <div class="footer-badge"><div class="brand-name">Morvesta<br>Group, LLC</div></div>

  <svg class="contact-icon" style="left:52px;top:1002px" width="13" height="17" viewBox="0 0 12 16" aria-hidden="true"><path d="M6 0 C2.7 0 0 2.6 0 5.8 C0 10 6 16 6 16 C6 16 12 10 12 5.8 C12 2.6 9.3 0 6 0 Z" fill="var(--blue)"/><circle cx="6" cy="5.8" r="2.2" fill="#fff"/></svg>
  <div class="contact" style="left:76px;top:1000px">418 N. Alder Lane,<br>Fenwick, MI 49012</div>
  <div class="divider" style="left:227px"></div>

  <svg class="contact-icon" style="left:243px;top:1009px" width="11" height="11" viewBox="0 0 16 16" aria-hidden="true"><path d="M3 1 L6 1 L7 5 L5 6.5 C6 9 7 10 9.5 11 L11 9 L15 10 L15 13 C15 14 14 15 13 15 C6 15 1 10 1 3 C1 2 2 1 3 1 Z" fill="none" stroke="var(--blue)" stroke-width="1.6"/></svg>
  <div class="contact" style="left:256px;top:1008px">(555) 214-0387</div>
  <div class="divider" style="left:367px"></div>

  <svg class="contact-icon" style="left:375px;top:1009px" width="12" height="9" viewBox="0 0 16 12" aria-hidden="true"><rect width="16" height="12" fill="var(--blue)"/><path d="M0 0 L8 7 L16 0" fill="none" stroke="#fff" stroke-width="1.4"/></svg>
  <div class="contact" style="left:393px;top:1007px">info@morvestagroup.com</div>
  <div class="divider" style="left:559px"></div>

  <svg class="contact-icon" style="left:568px;top:1008px" width="11" height="11" viewBox="0 0 16 16" aria-hidden="true"><circle cx="8" cy="8" r="7" fill="none" stroke="var(--blue)" stroke-width="1.5"/><ellipse cx="8" cy="8" rx="3" ry="7" fill="none" stroke="var(--blue)" stroke-width="1.2"/><path d="M1 8 H15 M2.5 4.5 H13.5 M2.5 11.5 H13.5" stroke="var(--blue)" stroke-width="1.2"/></svg>
  <div class="contact" style="left:583px;top:1007px">www.morvestagroup.com</div>
</main>
</body>
</html>
```